High End Notary Service Business Card Design

Want a professional and elegant/luxurious business card that is clean and simple in the design. A notary is a trusted professional that helps people sign very important documents. The card should be in alignment with this service provided.

Most of the time, service will be for the purchase of a home or refinance of a mortgage

There is NO LOGO. This is aesthetic. A look and feel. Conveying professionalism and concierge level of service.

Target Market(s)

Other business professionals, Lawyers, Escrow Officers, Loan Officers

Industry/Entity Type

Legal

Contact Information for Business Card

This will be a one-sided business card

Colors
35a7d7
3176b5
85cae6
d3a5cc
b868aa
ffffff
0356a4

Requirements
Must have
• Doreen L. Marsh-Whitlock
Notary Public

614-872-3916
MarshPublicNotary@Vornmail.com
Nice to have
• Headshot photo below. Convey the aspect of signing documents. No black cards. Preference is shades of blue: light blue, navy, aqua, gold, white, or lavendar, etc.
Should not have
• No scales or legal scales.

```html
<!DOCTYPE html>
<html lang="en">
<head>
<meta charset="utf-8">
<title>Doreen L. Marsh-Whitlock — Notary Public</title>
<link rel="stylesheet" href="https://fonts.googleapis.com/css2?family=Great+Vibes&family=Lato:wght@300;400&display=swap">
<style>
  :root {
    --page: #ffffff;
    --card-paper: #f8f4f3;
    --ink-blue: #4a78b5;
    --lavender: #b868aa;
    --lavender-soft: #d3a5cc;
    --sky: #85cae6;
    --aqua: #35a7d7;
    --navy: #0356a4;
    --photo-top: #8a8e9a;
    --photo-mid: #b08a70;
    --photo-low: #8fb86a;
  }
  * { box-sizing: border-box; margin: 0; padding: 0; }
  html, body {
    width: 1200px;
    height: 969px;
    overflow: hidden;
    background: var(--page);
  }
  .business-card {
    position: absolute;
    left: 50px;
    top: 128px;
    width: 1100px;
    height: 712px;
    background: var(--card-paper);
    font-family: "Lato", sans-serif;
    color: var(--ink-blue);
  }
  .headshot {
    position: absolute;
    left: 488px;
    top: 81px;
    width: 124px;
    height: 155px;
    background: linear-gradient(180deg, var(--photo-top) 0%, var(--photo-mid) 45%, var(--photo-low) 100%);
  }
  .signature-name {
    position: absolute;
    left: 0;
    top: 0;
    width: 100%;
    height: 100%;
    font-family: "Great Vibes", cursive;
    font-weight: 400;
    font-size: 78px;
    line-height: 80px;
    white-space: nowrap;
    pointer-events: none;
  }
  .signature-name span {
    position: absolute;
    background: linear-gradient(100deg, var(--lavender) 0%, var(--sky) 30%, var(--lavender) 55%, var(--navy) 75%, var(--lavender-soft) 100%);
    -webkit-background-clip: text;
    background-clip: text;
    color: transparent;
    padding: 0 12px;
  }
  .signature-name .first-line {
    left: 316px;
    top: 240px;
  }
  .signature-name .last-line {
    left: 396px;
    top: 310px;
  }
  .title {
    position: absolute;
    left: 0;
    width: 100%;
    top: 437px;
    text-align: center;
    font-size: 31px;
    font-weight: 400;
  }
  .contact {
    position: absolute;
    left: 0;
    width: 100%;
    top: 565px;
    text-align: center;
    font-weight: 300;
    font-size: 37px;
    line-height: 48px;
  }
  .contact span { display: block; white-space: nowrap; }
</style>
</head>
<body>
  <div class="business-card">
    <div class="headshot" role="img" aria-label="Headshot portrait of the notary"></div>
    <h1 class="signature-name">
      <span class="first-line">Doreen L.</span>
      <span class="last-line">Marsh-Whitlock</span>
    </h1>
    <p class="title">Notary Public</p>
    <p class="contact">
      <span class="phone">614-872-3916</span>
      <span class="email">MarshPublicNotary@Vornmail.com</span>
    </p>
  </div>
</body>
</html>
```